Flyer for a Payroll and Bookkeeping Companmy

Need a brochure to highlight our costs and service to hand out to clients.

Please see attachments for more information.

Industry/Entity Type

It Service

```html
<!DOCTYPE html>
<html lang="en">
<head>
<meta charset="utf-8">
<title>Summit Ridge – Pricing Flyers</title>
<link rel="stylesheet" href="https://fonts.googleapis.com/css2?family=Lato:wght@400;700;900&family=Montserrat:wght@700;900&display=swap">
<style>
  :root {
    --blue: #0a7fd4;
    --blue-dark: #0863a8;
    --orange: #f07d17;
    --orange-dark: #c8620c;
    --ink: #2e2e2e;
    --band: #ececec;
    --page: #ffffff;
    --backdrop: #e4e4e4;
  }
  * { box-sizing: border-box; margin: 0; padding: 0; }
  html, body { width: 1200px; height: 1200px; overflow: hidden; }
  body { background: var(--backdrop); font-family: "Lato", Arial, sans-serif; color: var(--ink); position: relative; }

  .flyer { position: absolute; left: 265px; width: 670px; height: 515px; background: var(--page); overflow: hidden; }
  .flyer--bookkeeping { top: 56px; }
  .flyer--payroll { top: 623px; }

  .brand { position: absolute; display: flex; flex-direction: column; }
  .brand-name { display: flex; align-items: center; gap: 6px; font: 700 21px/1 "Lato", sans-serif; color: var(--blue); }
  .brand-dot { width: 12px; height: 12px; border-radius: 50%; background: var(--orange); }
  .brand-tagline { margin-top: 3px; margin-left: 18px; font: 400 10.5px/1 "Lato", sans-serif; color: var(--orange); }
  .flyer--bookkeeping .brand { left: 51px; top: 62px; }
  .flyer--payroll .brand { left: 37px; top: 62px; }

  .flyer-title { position: absolute; font: 700 34px/1 "Lato", sans-serif; white-space: nowrap; }
  .flyer-title .accent { color: var(--orange); }
  .flyer-title .main { color: var(--blue); font-weight: 900; }
  .flyer--bookkeeping .flyer-title { right: 35px; top: 33px; }
  .flyer--payroll .flyer-title { right: 14px; top: 29px; font-size: 31px; }

  .pricing-table { position: absolute; top: 0; height: 480px; }
  .pricing-table--core { left: 35px; width: 272px; }
  .pricing-table--extras { left: 361px; width: 273px; }

  .table-head { position: absolute; top: 116px; left: 0; right: 0; height: 20px; }
  .services-label { position: absolute; left: 21px; top: 3px; font: 700 9.5px/1 "Montserrat", sans-serif; letter-spacing: .3px; }
  .tier { position: absolute; width: 60px; margin-left: -30px; text-align: center; }
  .tier-name { display: block; font: 700 6.6px/1.1 "Montserrat", sans-serif; }
  .tier-price { display: block; font: 700 9px/1.1 "Montserrat", sans-serif; color: var(--orange); }

  .price-row { position: absolute; left: 0; right: 0; background: var(--band); display: flex; }
  .row-1 { top: 137px; height: 49px; }
  .row-2 { top: 234px; height: 46px; }
  .row-3 { top: 328px; height: 46px; }
  .row-4 { top: 414px; height: 44px; }

  .row-ribbon { position: absolute; left: 11px; top: -3px; width: 62px; height: 76px; }
  .row-label { position: absolute; left: 11px; top: -3px; width: 57px; height: 56px; display: flex; flex-direction: column; align-items: center; justify-content: center; text-align: center; color: #fff; font: 700 8.4px/1.2 "Lato", sans-serif; }
  .row-label small { font-size: 5.5px; font-weight: 400; opacity: .85; }

  .row-cells { margin-left: 72px; flex: 1; display: flex; }
  .cell { flex: 1; display: flex; flex-direction: column; align-items: center; justify-content: center; text-align: center; font: 400 8.4px/1.15 "Lato", sans-serif; border-left: 2px solid #f7f7f7; }
  .cell:first-child { border-left: none; }
  .cell .tick { font-size: 12px; line-height: 1; font-weight: 700; }
  .cell .amount { font: 700 8.4px/1 "Montserrat", sans-serif; }
  .cell .none { font: 700 9px/1 "Montserrat", sans-serif; }

  .flyer-footer { position: absolute; left: 0; bottom: 0; width: 670px; height: 24px; }
  .flyer-footer svg { position: absolute; inset: 0; }
  .contact { position: absolute; top: 0; height: 24px; display: flex; align-items: center; gap: 4px; color: #fff; font: 400 9px/1 "Lato", sans-serif; white-space: nowrap; }
  .contact svg { position: static; width: 8px; height: 8px; }
  .contact--phone { left: 46px; }
  .contact--web { left: 139px; }
  .contact--address { left: 241px; }

  .payroll-backdrop { position: absolute; inset: 0 0 24px 0; background: linear-gradient(160deg, #ffffff 0%, #f3f4f6 45%, #eceef1 75%, #f6f6f7 100%); }
  .offer-bubble { position: absolute; left: 0; top: 0; width: 670px; height: 515px; }
  .offer { position: absolute; left: 150px; width: 400px; text-align: center; color: #fff; white-space: nowrap; }
  .offer-line-1 { top: 156px; }
  .offer-line-2 { top: 204px; }
  .offer-line-3 { top: 254px; font: 900 38px/1 "Montserrat", sans-serif; }
  .offer .figure { font: 900 35px/1 "Montserrat", sans-serif; color: var(--orange); }
  .offer .unit { font: 700 27px/1 "Lato", sans-serif; margin-left: 6px; }
  .offer-line-2 .unit { margin-left: 18px; }
  .fine-print { position: absolute; left: 35px; width: 600px; top: 445px; text-align: center; font: 400 8.6px/1.3 "Lato", sans-serif; color: #444; }
  .fine-print strong { font-weight: 700; color: var(--ink); }
  .fine-print .highlight { color: var(--orange); }
</style>
</head>
<body>

<!-- Bookkeeping pricing sheet -->
<section class="flyer flyer--bookkeeping">
  <div class="brand">
    <div class="brand-name"><span class="brand-dot"></span>Summit Ridge</div>
    <div class="brand-tagline">Payroll and Bookkeeping</div>
  </div>
  <h1 class="flyer-title"><span class="accent">Bookkeeping</span> <span class="main">Pricing</span></h1>

  <div class="pricing-table pricing-table--core">
    <div class="table-head">
      <span class="services-label">SERVICES</span>
      <span class="tier" style="left:100px"><span class="tier-name">Premium</span><span class="tier-price">$999</span></span>
      <span class="tier" style="left:156px"><span class="tier-name">Entrepreneur</span><span class="tier-price">$599</span></span>
      <span class="tier" style="left:201px"><span class="tier-name">Growth</span><span class="tier-price">$299</span></span>
      <span class="tier" style="left:249px"><span class="tier-name">Start Up</span><span class="tier-price">$149</span></span>
    </div>

    <div class="price-row row-1">
      <svg class="row-ribbon" viewBox="0 0 62 76"><polygon points="57,0 62,4 57,4" fill="var(--blue-dark)"/><polygon points="0,0 57,0 57,56 28.5,76 0,56" fill="var(--blue)"/></svg>
      <div class="row-label">Employees</div>
      <div class="row-cells">
        <div class="cell">Around<br>10+</div><div class="cell">Around<br>5-9</div><div class="cell">Around<br>2-5</div><div class="cell">Around<br>1-2</div>
      </div>
    </div>
    <div class="price-row row-2">
      <svg class="row-ribbon" viewBox="0 0 62 76"><polygon points="57,0 62,4 57,4" fill="var(--orange-dark)"/><polygon points="0,0 57,0 57,56 28.5,76 0,56" fill="var(--orange)"/></svg>
      <div class="row-label">Transactions/<br>Month</div>
      <div class="row-cells">
        <div class="cell">Up to<br>250</div><div class="cell">Up to<br>150</div><div class="cell">Up to<br>75</div><div class="cell">Up to<br>50</div>
      </div>
    </div>
    <div class="price-row row-3">
      <svg class="row-ribbon" viewBox="0 0 62 76"><polygon points="57,0 62,4 57,4" fill="var(--blue-dark)"/><polygon points="0,0 57,0 57,56 28.5,76 0,56" fill="var(--blue)"/></svg>
      <div class="row-label">Bookkeeping</div>
      <div class="row-cells">
        <div class="cell"><span class="tick">✓</span>Weekly</div><div class="cell"><span class="tick">✓</span>Weekly</div><div class="cell"><span class="tick">✓</span>Monthly</div><div class="cell"><span class="tick">✓</span>Quarterly</div>
      </div>
    </div>
    <div class="price-row row-4">
      <svg class="row-ribbon" viewBox="0 0 62 76"><polygon points="57,0 62,4 57,4" fill="var(--orange-dark)"/><polygon points="0,0 57,0 57,56 28.5,76 0,56" fill="var(--orange)"/></svg>
      <div class="row-label">Financial<br>Reports<br>&amp; Review</div>
      <div class="row-cells">
        <div class="cell"><span class="tick">✓</span>Monthly</div><div class="cell"><span class="tick">✓</span>Monthly</div><div class="cell"><span class="tick">✓</span>Monthly</div><div class="cell"><span class="tick">✓</span>Quarterly</div>
      </div>
    </div>
  </div>

  <div class="pricing-table pricing-table--extras">
    <div class="table-head">
      <span class="services-label">SERVICES</span>
      <span class="tier" style="left:101px"><span class="tier-name">Premium</span><span class="tier-price">$999</span></span>
      <span class="tier" style="left:152px"><span class="tier-name">Entrepreneur</span><span class="tier-price">$599</span></span>
      <span class="tier" style="left:204px"><span class="tier-name">Growth</span><span class="tier-price">$299</span></span>
      <span class="tier" style="left:248px"><span class="tier-name">Start Up</span><span class="tier-price">$149</span></span>
    </div>

    <div class="price-row row-1">
      <svg class="row-ribbon" viewBox="0 0 62 76"><polygon points="57,0 62,4 57,4" fill="var(--blue-dark)"/><polygon points="0,0 57,0 57,56 28.5,76 0,56" fill="var(--blue)"/></svg>
      <div class="row-label">Support<small>(Phone and Chat)</small></div>
      <div class="row-cells">
        <div class="cell"><span class="tick">✓</span></div><div class="cell"><span class="tick">✓</span></div><div class="cell"><span class="tick">✓</span></div><div class="cell"><span class="tick">✓</span></div>
      </div>
    </div>
    <div class="price-row row-2">
      <svg class="row-ribbon" viewBox="0 0 62 76"><polygon points="57,0 62,4 57,4" fill="var(--orange-dark)"/><polygon points="0,0 57,0 57,56 28.5,76 0,56" fill="var(--orange)"/></svg>
      <div class="row-label">Online<br>Collaboration<br>Portal<small>(Cloud Drive)</small></div>
      <div class="row-cells">
        <div class="cell"><span class="tick">✓</span></div><div class="cell"><span class="tick">✓</span></div><div class="cell"><span class="tick">✓</span></div><div class="cell"><span class="tick">✓</span></div>
      </div>
    </div>
    <div class="price-row row-3">
      <svg class="row-ribbon" viewBox="0 0 62 76"><polygon points="57,0 62,4 57,4" fill="var(--blue-dark)"/><polygon points="0,0 57,0 57,56 28.5,76 0,56" fill="var(--blue)"/></svg>
      <div class="row-label">Business<br>Tax Return</div>
      <div class="row-cells">
        <div class="cell"><span class="tick">✓</span></div><div class="cell"><span class="tick">✓</span></div><div class="cell"><span class="amount">$799</span></div><div class="cell"><span class="amount">$599</span></div>
      </div>
    </div>
    <div class="price-row row-4">
      <svg class="row-ribbon" viewBox="0 0 62 76"><polygon points="57,0 62,4 57,4" fill="var(--orange-dark)"/><polygon points="0,0 57,0 57,56 28.5,76 0,56" fill="var(--orange)"/></svg>
      <div class="row-label">Bill Pay</div>
      <div class="row-cells">
        <div class="cell"><span class="tick">✓</span><span class="amount" style="font-size:7px">$5 /<br>Payment</span></div><div class="cell"><span class="none">x</span></div><div class="cell"><span class="none">x</span></div><div class="cell"><span class="none">x</span></div>
      </div>
    </div>
  </div>

  <footer class="flyer-footer">
    <svg viewBox="0 0 670 24" width="670" height="24"><polygon points="0,0 453,0 466,24 0,24" fill="var(--blue)"/><polygon points="468,8 670,8 670,24 476,24" fill="var(--orange)"/></svg>
    <span class="contact contact--phone"><svg viewBox="0 0 10 10"><path d="M2 1l2 2-1 1.2c.6 1.2 1.6 2.2 2.8 2.8L7 6l2 2-1.3 1.3C4.5 9 1 5.5.7 2.3z" fill="#fff"/></svg>555-310-4427</span>
    <span class="contact contact--web"><svg viewBox="0 0 10 10"><circle cx="5" cy="5" r="4" fill="none" stroke="#fff" stroke-width="1"/><path d="M1 5h8M5 1c2 2.4 2 5.6 0 8M5 1c-2 2.4-2 5.6 0 8" fill="none" stroke="#fff" stroke-width=".8"/></svg>SummitRidgeBooks.com</span>
    <span class="contact contact--address"><svg viewBox="0 0 10 10"><path d="M5 0.5a3.2 3.2 0 0 1 3.2 3.2C8.2 6 5 9.5 5 9.5S1.8 6 1.8 3.7A3.2 3.2 0 0 1 5 .5z" fill="#fff"/><circle cx="5" cy="3.7" r="1.1" fill="var(--blue)"/></svg>1280 Alder Ave, Riverton, UT 84065</span>
  </footer>
</section>

<!-- Payroll pricing sheet -->
<section class="flyer flyer--payroll">
  <div class="payroll-backdrop" role="img" aria-label="Faded office desk photo with paperwork in soft white and grey tones"></div>
  <div class="brand">
    <div class="brand-name"><span class="brand-dot"></span>Summit Ridge</div>
    <div class="brand-tagline">Payroll and Bookkeeping</div>
  </div>
  <h1 class="flyer-title"><span class="accent">Simplified</span> <span class="main">Payroll Pricing</span></h1>

  <svg class="offer-bubble" viewBox="0 0 670 515">
    <path d="M156 133 L545 141 Q556 142 555 154 L546 323 Q545 335 533 337 L452 383 L363 423 L392 387 L185 381 Q174 380 171 368 L154 147 Q153 133 156 133 Z" fill="#cfd2d6"/>
    <path d="M474 81 L491 129 L527 129 Z" fill="var(--blue-dark)"/>
    <path d="M155 121 L528 129 Q542 130 541 144 L533 306 Q532 320 518 322 L439 373 L350 413 L379 377 L181 369 Q170 368 168 356 L140 136 Q139 121 155 121 Z" fill="var(--blue)"/>
  </svg>
  <p class="offer offer-line-1"><span class="figure">$25</span><span class="unit">per Payroll</span></p>
  <p class="offer offer-line-2"><span class="figure">+$5</span><span class="unit">per Employee</span></p>
  <p class="offer offer-line-3">No Set Up Fees!</p>

  <p class="fine-print">Direct deposit only, add <strong>$20</strong> per payroll if you elect to have paper checks shipped to you. Minimum charge of two payrolls per month. <span class="highlight">Cost per employee drops to $4 after 20 employees.</span></p>

  <footer class="flyer-footer">
    <svg viewBox="0 0 670 24" width="670" height="24"><polygon points="0,0 453,0 466,24 0,24" fill="var(--blue)"/><polygon points="468,8 670,8 670,24 476,24" fill="var(--orange)"/></svg>
    <span class="contact contact--phone"><svg viewBox="0 0 10 10"><path d="M2 1l2 2-1 1.2c.6 1.2 1.6 2.2 2.8 2.8L7 6l2 2-1.3 1.3C4.5 9 1 5.5.7 2.3z" fill="#fff"/></svg>555-310-4427</span>
    <span class="contact contact--web"><svg viewBox="0 0 10 10"><circle cx="5" cy="5" r="4" fill="none" stroke="#fff" stroke-width="1"/><path d="M1 5h8M5 1c2 2.4 2 5.6 0 8M5 1c-2 2.4-2 5.6 0 8" fill="none" stroke="#fff" stroke-width=".8"/></svg>SummitRidgeBooks.com</span>
    <span class="contact contact--address"><svg viewBox="0 0 10 10"><path d="M5 0.5a3.2 3.2 0 0 1 3.2 3.2C8.2 6 5 9.5 5 9.5S1.8 6 1.8 3.7A3.2 3.2 0 0 1 5 .5z" fill="#fff"/><circle cx="5" cy="3.7" r="1.1" fill="var(--blue)"/></svg>1280 Alder Ave, Riverton, UT 84065</span>
  </footer>
</section>

</body>
</html>
```